Redesign Website - Current one too plain

The description is in the uploaded file. Please let me know if you need any more information. I'd prefer it if someone could implement the design to a WordPress site but the best design will win, regardless.
I would like the forms to look nice as well
UPDATE:
I don't think we can use the images that I provided, I think they make the site look a bit 'cheap' and I really don't know how to replace them. One thought I have had is to make the "Simple, Unique, Effective" a second feature on the right side of the page with the search on the left
Target Market(s)
Small companies, private sellers of cars and people who rent their caravan/holiday home out
Industry/Entity Type
Advertising
Number of Pages Required
3 page
Colors
Designer to choose colors to be used in the design.
Look and feel

```html
<!DOCTYPE html>
<html lang="en">
<head>
<meta charset="utf-8">
<title>KODRA — Find advertisers by code</title>
<link rel="stylesheet" href="https://fonts.googleapis.com/css2?family=Outfit:wght@400;500;600;700&family=Archivo:wdth,wght@125,900&display=swap">
<style>
  :root {
    --ink: #111111;
    --paper: #ffffff;
    --lime: #e4ff14;
    --pill: #ececec;
    --chevron: #6b6b6b;
    --hero-sky: #b4c4d0;
    --hero-green: #6f7a55;
    --hero-road: #3a3c44;
    --hero-deep: #2c2d34;
  }
  * { box-sizing: border-box; margin: 0; padding: 0; }
  html, body { width: 1200px; height: 1068px; overflow: hidden; background: var(--paper); }
  body { position: relative; font-family: "Outfit", sans-serif; color: var(--ink); }

  .site-nav {
    position: absolute; left: 21px; top: 22px; width: 1159px; height: 75px;
    background: var(--ink); border-radius: 15px;
  }
  .brand {
    position: absolute; left: 52px; top: 24px; display: flex; align-items: center; gap: 8px;
    color: var(--lime); font-size: 22px; font-weight: 500; letter-spacing: 3px; line-height: 26px;
  }
  .brand-dot { width: 14px; height: 14px; border-radius: 50%; background: var(--lime); }
  .nav-links {
    position: absolute; left: 450px; top: 0; height: 75px; display: flex; align-items: center; gap: 20px;
    list-style: none; font-size: 14px; font-weight: 500;
  }
  .nav-links a { color: var(--paper); text-decoration: none; }
  .nav-links a.is-active { color: var(--lime); font-weight: 600; }
  .login-btn {
    position: absolute; left: 982px; top: 17px; width: 130px; height: 41px;
    border: 1px solid var(--paper); border-radius: 21px; color: var(--paper);
    display: flex; align-items: center; justify-content: center; font-size: 15px; font-weight: 500;
  }

  .hero {
    position: absolute; left: 21px; top: 107px; width: 1159px; height: 605px;
    border-radius: 22px; overflow: hidden;
  }
  .hero-photo {
    position: absolute; inset: 0;
    background: linear-gradient(170deg, var(--hero-sky) 0%, var(--hero-green) 40%, var(--hero-road) 68%, var(--hero-deep) 100%);
  }

  .code-card {
    position: absolute; left: 53px; top: 68px; width: 464px; height: 470px;
    border-radius: 45px; background: linear-gradient(180deg, #e4eef5 0%, #f7f8f9 45%, #fafafa 100%);
  }
  .chevron { position: absolute; width: 22px; height: 12px; }
  .code-display {
    position: absolute; left: 0; width: 100%; top: 92px; text-align: center;
    font-family: "Archivo", sans-serif; font-weight: 900; font-stretch: 125%;
    font-size: 164px; line-height: 160px; letter-spacing: 4px;
  }
  .category-pills { position: absolute; left: 33px; top: 292px; display: flex; gap: 6px; }
  .pill {
    width: 129px; height: 45px; border-radius: 23px; background: var(--pill);
    display: flex; align-items: center; justify-content: center; font-size: 15px;
  }
  .search-btn {
    position: absolute; left: 152px; top: 380px; width: 160px; height: 41px; border-radius: 21px;
    background: var(--lime); display: flex; align-items: center; justify-content: space-between;
    padding: 0 16px 0 28px; font-size: 15px; font-weight: 500;
  }
  .advertise-btn {
    position: absolute; left: 763px; top: 495px; width: 254px; height: 42px; border-radius: 21px;
    background: var(--lime); display: flex; align-items: center; justify-content: center; gap: 16px;
    font-size: 15px; font-weight: 500;
  }

  .features {
    position: absolute; left: 21px; top: 725px; width: 1159px; height: 261px;
    border-radius: 22px; background: var(--lime);
  }
  .features-heading { position: absolute; left: 139px; top: 102px; line-height: 1; }
  .features-heading .lead { display: block; font-size: 27px; font-weight: 400; }
  .features-heading .main { display: block; font-size: 45px; font-weight: 600; margin-top: 4px; }
  .feature { position: absolute; top: 54px; width: 190px; }
  .feature svg { width: 36px; height: 36px; display: block; }
  .feature h3 { font-size: 27px; font-weight: 700; margin-top: 20px; line-height: 1; }
  .feature p { font-size: 15px; line-height: 17px; margin-top: 14px; }

  .site-footer {
    position: absolute; left: 162px; top: 1017px; width: 875px;
    display: flex; justify-content: space-between; font-size: 15px;
  }
  .site-footer a { color: var(--ink); text-decoration: none; }
</style>
</head>
<body>
  <nav class="site-nav">
    <div class="brand"><span class="brand-dot"></span>KODRA</div>
    <ul class="nav-links">
      <li><a href="#" class="is-active">Home</a></li>
      <li><a href="#">Advertise</a></li>
      <li><a href="#">Contact</a></li>
      <li><a href="#">Register</a></li>
    </ul>
    <a class="login-btn">LOGIN</a>
  </nav>

  <section class="hero">
    <div class="hero-photo" role="img" aria-label="Photo: red hatchback driving along a road lined with trees under a cloudy sky"></div>
    <div class="code-card">
      <svg class="chevron" style="left:156px;top:66px" viewBox="0 0 22 12"><path d="M2 11 11 2l9 9" fill="none" stroke="var(--chevron)" stroke-width="2.2"/></svg>
      <svg class="chevron" style="left:313px;top:66px" viewBox="0 0 22 12"><path d="M2 11 11 2l9 9" fill="none" stroke="var(--chevron)" stroke-width="2.2"/></svg>
      <div class="code-display">A1</div>
      <svg class="chevron" style="left:156px;top:250px" viewBox="0 0 22 12"><path d="M2 1l9 9 9-9" fill="none" stroke="var(--chevron)" stroke-width="2.2"/></svg>
      <svg class="chevron" style="left:313px;top:250px" viewBox="0 0 22 12"><path d="M2 1l9 9 9-9" fill="none" stroke="var(--chevron)" stroke-width="2.2"/></svg>
      <div class="category-pills">
        <span class="pill">Car</span><span class="pill">Caravan</span><span class="pill">Company</span>
      </div>
      <a class="search-btn">Search
        <svg width="18" height="18" viewBox="0 0 18 18"><circle cx="8" cy="8" r="6" fill="none" stroke="var(--ink)" stroke-width="1.6"/><path d="M12.5 12.5 16 16" stroke="var(--ink)" stroke-width="1.6"/></svg>
      </a>
    </div>
    <a class="advertise-btn">Advertise Your Company
      <svg width="18" height="14" viewBox="0 0 18 14"><path d="M1 7h15M10 1l6 6-6 6" fill="none" stroke="var(--ink)" stroke-width="1.8"/></svg>
    </a>
  </section>

  <section class="features">
    <h2 class="features-heading"><span class="lead">Our Core</span><span class="main">Features</span></h2>
    <div class="feature" style="left:422px">
      <svg viewBox="0 0 36 36" fill="none" stroke="var(--ink)" stroke-width="1.5"><circle cx="17" cy="17" r="15"/><circle cx="17" cy="17" r="10"/><circle cx="17" cy="17" r="5"/><path d="M17 17l14 14M26 31h5v-5"/></svg>
      <h3>Simple</h3>
      <p>Create &nbsp;your<br>advert &amp; display<br>your code.</p>
    </div>
    <div class="feature" style="left:613px">
      <svg viewBox="0 0 36 36" fill="none" stroke="var(--ink)" stroke-width="1.5"><circle cx="18" cy="18" r="11"/><path d="M18 2v5M18 29v5M2 18h5M29 18h5M6.7 6.7l3.5 3.5M25.8 25.8l3.5 3.5M6.7 29.3l3.5-3.5M25.8 10.2l3.5-3.5"/><path d="M18 11l2.2 4.5 4.8.6-3.5 3.3.9 4.8-4.4-2.4-4.4 2.4.9-4.8-3.5-3.3 4.8-.6z"/></svg>
      <h3>Unique</h3>
      <p>Customers find you<br>by an easy-to-remember<br>code.</p>
    </div>
    <div class="feature" style="left:857px">
      <svg viewBox="0 0 36 36" fill="none" stroke="var(--ink)" stroke-width="1.5"><path d="M2 24l9-9 6 6 15-15M24 5h9v9"/><path d="M4 34v-6M11 34v-11M18 34v-8M25 34v-13M32 34v-17"/></svg>
      <h3>Effective</h3>
      <p>Customers are directed<br>to you and not a list of<br>your competitors.</p>
    </div>
  </section>

  <footer class="site-footer">
    <span>© 2023 <strong>KODRA.</strong> All rights reserved.</span>
    <span><a href="#">Terms &amp; Conditions</a> &nbsp;| &nbsp;<a href="#">Privacy Policy</a></span>
  </footer>
</body>
</html>
```